velmora LED lighting Brochure design *

need a Brochure for velmora LED, that is a company specialises in industrial LED lighting solutions ... we also do retail, gas stations as well...
we are formed to serve customer need in lighting doing engineering, supply and installation of LED lighting
we need a Brochure that describe our company work, project cycle, project reference and services provided in addition to our main products that will be provided to consultant for product range approval

Target Market(s)

industrial sector (petrochemical, chemical, factories), construction, retail shops, gas stations

Industry/Entity Type

Lighting

Colors

Requirements
Must have
• project cycle
• project reference photos... cant upload it here

```html
<!DOCTYPE html>
<html lang="en">
<head>
<meta charset="utf-8">
<title>velmora LED – Flood Light Spread</title>
<link rel="stylesheet" href="https://fonts.googleapis.com/css2?family=Heebo:wght@300;400;700&display=swap">
<style>
  :root {
    --red: #e8202a;
    --ink: #1a1a1a;
    --grey: #6b6b6b;
    --rule: #d4d4d4;
    --paper: #ffffff;
    --photo: #34374a;
    --product: #3c3f44;
    --navy: #1d2a4a;
  }
  html, body { margin: 0; padding: 0; overflow: hidden; background: var(--paper); }
  .canvas { width: 1200px; height: 849px; position: relative; font-family: "Heebo", sans-serif; }
  .spread { position: absolute; inset: 0; }
  .page-label { font-size: 17px; fill: var(--ink); font-weight: 400; }
  .title { font-size: 35px; font-weight: 300; fill: var(--red); }
  .intro { font-size: 12.5px; font-weight: 300; fill: var(--grey); }
  .section-head { font-size: 17px; font-weight: 300; fill: var(--navy); }
  .section-text { font-size: 9px; font-weight: 300; fill: var(--grey); }
  .site { font-size: 9px; font-weight: 700; fill: var(--ink); }
  .brand { font-size: 10px; font-weight: 700; fill: var(--navy); }
  .ring { fill: none; stroke: var(--red); stroke-width: 4.5; }
  .th { font-size: 9px; font-weight: 700; fill: #fff; }
  .td-label { font-size: 7.5px; font-weight: 300; fill: var(--grey); }
  .td { font-size: 7.5px; font-weight: 300; fill: var(--grey); text-anchor: middle; }
  .row-rule { stroke: var(--rule); stroke-width: 0.7; }
</style>
</head>
<body>
<div class="canvas">
<svg class="spread" width="1200" height="849" viewBox="0 0 1200 849" xmlns="http://www.w3.org/2000/svg">
  <defs>
    <filter id="pageShadow" x="-5%" y="-5%" width="110%" height="110%">
      <feDropShadow dx="0" dy="0" stdDeviation="3" flood-color="#000" flood-opacity="0.25"/>
    </filter>
  </defs>

  <text class="page-label" x="303" y="41" text-anchor="middle">Page-5</text>
  <text class="page-label" x="865" y="41" text-anchor="middle">Page-6</text>

  <!-- pages -->
  <rect x="34" y="65" width="558" height="722" fill="var(--paper)" filter="url(#pageShadow)"/>
  <rect x="595" y="65" width="558" height="722" fill="var(--paper)" filter="url(#pageShadow)"/>

  <!-- corner decoration areas -->
  <rect x="40" y="71" width="71" height="35" rx="4" fill="#2a8fa8" opacity="0.8" role="img" aria-label="Coloured dot cluster decoration"/>
  <rect x="1076" y="71" width="71" height="35" rx="4" fill="#2a8fa8" opacity="0.8" role="img" aria-label="Coloured dot cluster decoration"/>

  <!-- project photo across spread -->
  <rect x="355" y="111" width="237" height="630" fill="var(--photo)" role="img" aria-label="Project photo: sports pitch under floodlights at night"/>
  <rect x="595" y="111" width="237" height="630" fill="var(--photo)" role="img" aria-label="Project photo: sports pitch under floodlights at night"/>
  <rect x="591" y="65" width="4" height="722" fill="#9a9a9a"/>

  <!-- left page text -->
  <text class="title" x="80" y="211">Flood Light</text>
  <text class="intro">
    <tspan x="80" y="248">An Industrial grade Flood Light has an</tspan>
    <tspan x="80" y="266">innovation design and different optics for</tspan>
    <tspan x="80" y="284">the best performance in the lighting</tspan>
    <tspan x="80" y="302">distribution.</tspan>
  </text>

  <!-- product rings -->
  <circle class="ring" cx="354" cy="457" r="139"/>
  <circle class="ring" cx="354" cy="457" r="128"/>
  <circle class="ring" cx="354" cy="457" r="117"/>
  <circle cx="354" cy="457" r="104" fill="var(--paper)"/>
  <rect x="280" y="382" width="150" height="150" rx="14" fill="var(--product)" role="img" aria-label="Product photo: LED flood light fixture"/>

  <text class="section-head" x="80" y="627">Area of Application</text>
  <text class="section-text" x="80" y="645">Freight yards, Board illumination, Ports and airports,</text>
  <text class="section-text" x="80" y="663">Landscape lighting</text>
  <text class="site" x="80" y="766">velmoraled.com</text>

  <!-- spec table -->
  <g class="spec-table">
    <rect x="716" y="259" width="392" height="334" fill="var(--paper)" stroke="var(--red)" stroke-width="1.2"/>
    <rect x="716" y="259" width="392" height="23" fill="var(--red)"/>
    <line x1="832" y1="259" x2="832" y2="282" stroke="#fff" stroke-width="0.8"/>
    <line x1="900" y1="259" x2="900" y2="282" stroke="#fff" stroke-width="0.8"/>
    <line x1="970" y1="259" x2="970" y2="282" stroke="#fff" stroke-width="0.8"/>
    <line x1="1040" y1="259" x2="1040" y2="282" stroke="#fff" stroke-width="0.8"/>
    <text class="th" x="730" y="274">Watts</text>
    <text class="th" x="866" y="274" text-anchor="middle">100</text>
    <text class="th" x="935" y="274" text-anchor="middle">150</text>
    <text class="th" x="1004" y="274" text-anchor="middle">200</text>
    <text class="th" x="1074" y="274" text-anchor="middle">230</text>

    <line x1="832" y1="282" x2="832" y2="593" stroke="var(--rule)" stroke-width="0.7"/>
    <g>
      <line class="row-rule" x1="716" y1="306" x2="1108" y2="306"/>
      <line class="row-rule" x1="716" y1="322.4" x2="1108" y2="322.4"/>
      <line class="row-rule" x1="716" y1="338.8" x2="1108" y2="338.8"/>
      <line class="row-rule" x1="716" y1="355.2" x2="1108" y2="355.2"/>
      <line class="row-rule" x1="716" y1="371.6" x2="1108" y2="371.6"/>
      <line class="row-rule" x1="716" y1="388" x2="1108" y2="388"/>
      <line class="row-rule" x1="716" y1="404.4" x2="1108" y2="404.4"/>
      <line class="row-rule" x1="716" y1="420.8" x2="1108" y2="420.8"/>
      <line class="row-rule" x1="716" y1="437.2" x2="1108" y2="437.2"/>
      <line class="row-rule" x1="716" y1="453.6" x2="1108" y2="453.6"/>
      <line class="row-rule" x1="716" y1="470" x2="1108" y2="470"/>
      <line class="row-rule" x1="716" y1="486.4" x2="1108" y2="486.4"/>
      <line class="row-rule" x1="716" y1="502.8" x2="1108" y2="502.8"/>
      <line class="row-rule" x1="716" y1="519.2" x2="1108" y2="519.2"/>
      <line class="row-rule" x1="716" y1="535.6" x2="1108" y2="535.6"/>
      <line class="row-rule" x1="716" y1="552" x2="1108" y2="552"/>
      <line class="row-rule" x1="716" y1="568.4" x2="1108" y2="568.4"/>
      <line class="row-rule" x1="900" y1="404.4" x2="900" y2="420.8"/>
      <line class="row-rule" x1="970" y1="404.4" x2="970" y2="420.8"/>
      <line class="row-rule" x1="1040" y1="404.4" x2="1040" y2="420.8"/>
    </g>

    <text class="td-label" x="729" y="301">Input Voltage</text>
    <text class="td-label" x="729" y="317.4">Frequency Range</text>
    <text class="td-label" x="729" y="333.8">Total Harmonic Distortion</text>
    <text class="td-label" x="729" y="350.2">Power Factor</text>
    <text class="td-label" x="729" y="366.6">Power Efficiency</text>
    <text class="td-label" x="729" y="383">LED CHIP</text>
    <text class="td-label" x="729" y="399.4">LED Luminous Efficiency</text>
    <text class="td-label" x="729" y="415.8">LED Total Flux</text>
    <text class="td-label" x="729" y="432.2">Lamp's Efficiency</text>
    <text class="td-label" x="729" y="448.6">Illuminance Uniformity</text>
    <text class="td-label" x="729" y="465">Color Temperature</text>
    <text class="td-label" x="729" y="481.4">Color Rendering Index</text>
    <text class="td-label" x="729" y="497.8">Light Distribution</text>
    <text class="td-label" x="729" y="514.2">Working Temperature</text>
    <text class="td-label" x="729" y="530.6">IP Grade</text>
    <text class="td-label" x="729" y="547">Working Life-span</text>
    <text class="td-label" x="729" y="563.4">Certificate</text>

    <text class="td" x="970" y="301">220-240 / 110-220 Vac</text>
    <text class="td" x="970" y="317.4">50Hz-60Hz</text>
    <text class="td" x="970" y="333.8">≤9%</text>
    <text class="td" x="970" y="350.2">&gt;0.95</text>
    <text class="td" x="970" y="366.6">&gt;91%</text>
    <text class="td" x="970" y="383">KORVIN</text>
    <text class="td" x="970" y="399.4">110-120Lm/W</text>
    <text class="td" x="866" y="415.8">11000-12000</text>
    <text class="td" x="935" y="415.8">16000-18000</text>
    <text class="td" x="1004" y="415.8">22000-24000</text>
    <text class="td" x="1074" y="415.8">25000-27600</text>
    <text class="td" x="970" y="432.2">100%</text>
    <text class="td" x="970" y="448.6">&gt;0.7</text>
    <text class="td" x="970" y="465">2700-6500K</text>
    <text class="td" x="970" y="481.4">Ra&gt;80</text>
    <text class="td" x="970" y="497.8">Symmetrical</text>
    <text class="td" x="970" y="514.2">-30 +55</text>
    <text class="td" x="970" y="530.6">IP65</text>
    <text class="td" x="970" y="547">&gt;50000H</text>
    <text class="td" x="970" y="563.4">CB, EER, IECEE,SABER</text>
  </g>

  <!-- brand name -->
  <rect x="1052" y="757" width="8" height="8" fill="var(--navy)"/>
  <text class="brand" x="1064" y="765">velmora LED</text>
</svg>
</div>
</body>
</html>
```